Business Cards that are elegant and wow

I want to create and print business cards that represent my brand and stand out from the rest. We want to ensure they stay in our branding and the integrity is not lost. I am happy to look at different shapes like square etc.

It will be printed on very thick cards and will be stylish .

I want to create and print business cards that represent my brand and stand out from the rest. We want to ensure they stay in ur branding and the integrity is not lost. I am happy to look at different shapes like square etc.

Target Market(s)

real estate professionals

Industry/Entity Type

Real Estate

Contact Information for Business Card

Maren Holt
hello@brightfernrealty.com.au
brightfernrealty.com.au
0487 316 252 (SMS)

Colors

Designer to choose colors to be used in the design.

Requirements
Must have
• My logo
• email
• website
• Name
Nice to have
• I like the idea of printing with foil or spot gloss. You want it to stand out in a sea.
Should not have
• I would like you to stay in my colour themes. Don't change the colour of my logo

```html
<!DOCTYPE html>
<html lang="en">
<head>
<meta charset="utf-8">
<title>Bright Fern Realty – Business Cards</title>
<link rel="stylesheet" href="https://fonts.googleapis.com/css2?family=Montserrat:wght@500&family=Oswald:wght@500&family=PT+Sans:wght@400;700&display=swap">
<style>
  :root {
    --backdrop: #ecebe7;
    --card: #2a2a2c;
    --card-sheen: #333336;
    --brand-blue: #3aa8e0;
    --brand-pink: #e6317b;
    --ink-light: #f2f2f2;
  }
  * { box-sizing: border-box; margin: 0; padding: 0; }
  html, body {
    width: 1200px; height: 1200px; overflow: hidden;
    background: var(--backdrop);
  }
  .sheet {
    width: 1200px; height: 1200px;
    display: flex; flex-direction: column;
    align-items: center; justify-content: center;
    gap: 60px;
  }
  .card {
    width: 900px; height: 514px;
    background: linear-gradient(115deg, var(--card) 0%, var(--card) 60%, var(--card-sheen) 100%);
    border-radius: 4px;
    box-shadow: 0 10px 28px rgba(0,0,0,0.22);
    display: flex; flex-direction: column;
    align-items: center; justify-content: center;
  }
  .brand-lockup {
    display: flex; align-items: center; gap: 22px;
  }
  .brand-dot {
    width: 96px; height: 96px;
    border: 7px solid var(--brand-blue);
    border-radius: 50%;
  }
  .brand-name {
    font-family: "Montserrat", sans-serif;
    font-weight: 500;
    color: var(--brand-blue);
    font-size: 50px;
    letter-spacing: 1px;
    text-transform: uppercase;
    line-height: 1;
  }
  .card--back .brand-lockup { flex-direction: column; gap: 26px; }
  .card--back .brand-dot { width: 150px; height: 150px; border-width: 8px; }
  .card--back .brand-name { font-size: 46px; }
  .holder-name {
    margin-top: 40px;
    font-family: "Oswald", sans-serif;
    font-weight: 500;
    color: var(--brand-blue);
    font-size: 40px;
    letter-spacing: 2px;
    text-transform: uppercase;
    line-height: 1;
  }
  .contact-icons {
    display: flex; gap: 12px; margin: 12px 0 10px;
  }
  .contact-icons svg { width: 16px; height: 16px; }
  .contact-lines {
    font-family: "PT Sans", sans-serif;
    color: var(--ink-light);
    font-size: 22px;
    letter-spacing: 1.5px;
    text-align: center;
    line-height: 1.3;
  }
  .contact-lines .web-core { color: var(--brand-blue); font-weight: 700; }
</style>
</head>
<body>
<main class="sheet">
  <section class="card card--front">
    <div class="brand-lockup">
      <div class="brand-dot"></div>
      <div class="brand-name">Bright Fern Realty</div>
    </div>
  </section>

  <section class="card card--back">
    <div class="brand-lockup">
      <div class="brand-dot"></div>
      <div class="brand-name">Bright Fern Realty</div>
    </div>
    <div class="holder-name">Maren Holt</div>
    <div class="contact-icons">
      <svg viewBox="0 0 16 16" aria-label="phone"><path d="M4 1.5 6 4 4.8 5.6a8 8 0 0 0 5.6 5.6L12 10l2.5 2-1.4 2.2C7.5 14 2 8.5 1.8 2.9Z" fill="none" stroke="var(--brand-pink)" stroke-width="1.5" stroke-linejoin="round"/></svg>
      <svg viewBox="0 0 16 16" aria-label="email"><rect x="1" y="3" width="14" height="10" fill="var(--brand-pink)"/><path d="M1 3 8 9 15 3" fill="none" stroke="var(--card)" stroke-width="1.3"/></svg>
      <svg viewBox="0 0 16 16" aria-label="website"><g fill="none" stroke="var(--brand-pink)" stroke-width="1.2"><circle cx="8" cy="8" r="6.5"/><ellipse cx="8" cy="8" rx="3" ry="6.5"/><path d="M1.5 8h13M2.5 4.8h11M2.5 11.2h11"/></g></svg>
    </div>
    <div class="contact-lines">
      <p>+0487 316 252 (SMS)</p>
      <p>hello@brightfernrealty.com.au</p>
      <p>www.<span class="web-core">brightfernrealty</span>.com.au</p>
    </div>
  </section>
</main>
</body>
</html>
```